Halvick Ledgers & Advisory Tri-Fold Brochure (8.5"x11")

I need a professional looking brochure for my bookkeeping business. I am looking for something professional yet casual (not too corporate looking). I have attached a sample brochure that will outline the areas and a copy of our logo. I'd like to stick with shades of blue. The final product should communicate professional and personal.

Target Market(s)

Small service businesses.

Industry/Entity Type

Business

Font styles to use
Sans Serif

Requirements
Must have
• Professional looking photos of people in areas where it asks for a picture.

```html
<!DOCTYPE html>
<html lang="en">
<head>
<meta charset="utf-8">
<title>Halvick Ledgers &amp; Advisory — Tri-Fold Brochure</title>
<link rel="stylesheet" href="https://fonts.googleapis.com/css2?family=Cinzel:wght@400;600&family=Tinos:wght@400;700&display=swap">
<style>
  :root{
    --page:#e9e6e1;
    --white:#ffffff;
    --ink:#1c2c44;
    --dark:#2a2b2d;
    --dark-deep:#1b1c1e;
    --blue:#1f8fd6;
    --blue-bright:#35b1ea;
    --blue-deep:#0c4f93;
    --text-light:#f2f4f6;
    --heading:"Cinzel", serif;
    --body:"Tinos", serif;
  }
  *{box-sizing:border-box;margin:0;padding:0}
  html,body{width:797px;height:1200px;overflow:hidden;background:var(--page)}
  .canvas{position:relative;width:797px;height:1200px}
  .sheet{position:absolute;left:45px;width:717px;background:var(--white);overflow:hidden;box-shadow:0 2px 8px rgba(0,0,0,.25)}
  .sheet--outside{top:30px;height:558px}
  .sheet--inside{top:613px;height:559px}
  .sheet-art{position:absolute;inset:0;width:100%;height:100%}
  .txt{position:absolute;font-family:var(--body);font-size:10.5px;line-height:1.18;color:var(--text-light)}
  .h{font-family:var(--heading);font-weight:400;position:absolute;line-height:1.1}
  .pill{position:absolute;background:linear-gradient(180deg,var(--blue-bright),var(--blue));color:#fff;font-family:var(--heading);border-radius:0 16px 16px 0;display:flex;align-items:center;box-shadow:0 1px 3px rgba(0,0,0,.4)}
  .justify{text-align:justify}
  .blue{color:var(--blue-bright)}
  .ink{color:var(--ink)}
  .dots{list-style:none}
  .dots li{position:relative;padding-left:13px;margin-bottom:3px}
  .dots li::before{content:"";position:absolute;left:0;top:4px;width:6px;height:6px;border-radius:50%;background:var(--blue-bright)}
  .brand{font-family:var(--heading);font-weight:400;color:var(--blue);display:flex;align-items:center;gap:6px;position:absolute}
  .brand-mark{display:inline-block;background:var(--blue)}
  .contact{position:absolute;left:255px;width:155px;text-align:center;font-family:var(--body);font-size:9.5px;color:var(--text-light)}
  .contact p{margin-top:3px}
  .contact .ico{display:inline-block;width:6px;height:6px;border-radius:50%;background:var(--blue-bright);margin-right:4px;vertical-align:middle}
</style>
</head>
<body>
<div class="canvas">

  <section class="sheet sheet--outside">
    <svg class="sheet-art" viewBox="0 0 717 558" preserveAspectRatio="none">
      <defs>
        <linearGradient id="darkPanel" x1="0" y1="0" x2="1" y2="0">
          <stop offset="0" stop-color="#36373a"/><stop offset="1" stop-color="#1c1d1f"/>
        </linearGradient>
        <linearGradient id="blueBand" x1="0" y1="0" x2="1" y2="0">
          <stop offset="0" stop-color="#0c4f93"/><stop offset="1" stop-color="#2aa7e0"/>
        </linearGradient>
        <linearGradient id="photoCool" x1="0" y1="0" x2="1" y2="1">
          <stop offset="0" stop-color="#c9d7e4"/><stop offset="1" stop-color="#7fa6cc"/>
        </linearGradient>
        <linearGradient id="photoWarm" x1="0" y1="0" x2="1" y2="1">
          <stop offset="0" stop-color="#d9c7a9"/><stop offset="1" stop-color="#8b7a66"/>
        </linearGradient>
      </defs>
      <path d="M0 0H400C410 180 430 380 480 558H0Z" fill="url(#darkPanel)"/>
      <path d="M0 0H420C300 6 160 18 0 52Z" fill="url(#blueBand)"/>
      <path d="M405 40C520 30 640 90 717 140V320C620 300 520 330 465 345C440 240 420 130 405 40Z" fill="url(#photoCool)" role="img" aria-label="Photo: hands reviewing financial charts on a tablet at a desk"/>
      <path d="M405 40C520 30 640 90 717 140V150C640 102 520 42 405 48Z" fill="#35b1ea"/>
      <path d="M465 345C540 320 640 300 717 320V440C640 455 560 470 480 500C475 450 470 400 465 345Z" fill="url(#blueBand)"/>
      <path d="M480 500C560 470 650 455 717 445V470C640 478 560 500 490 548Z" fill="#2b2c2e"/>
      <path d="M0 365C80 345 180 350 245 360V558H0Z" fill="url(#photoWarm)" role="img" aria-label="Photo: business team working with a laptop and papers at a meeting table"/>
    </svg>

    <h1 class="h" style="left:20px;top:52px;font-size:22px;color:#fff">Here to Simplify</h1>
    <p class="h blue" style="left:20px;top:77px;font-size:13px">The Bookkeeping Process</p>
    <div class="pill" style="left:0;top:110px;width:176px;height:32px;padding-left:26px;font-size:18px">What We Do</div>
    <p class="txt justify" style="left:22px;top:160px;width:234px">We allow business owners to spend more time focusing on their core business by providing comprehensive bookkeeping and business consulting services. We provide the financial data and tools that allow businesses to maximize profitability and focus on growth and other areas of their business. We consider our business to be an extension of your business and look forward to the opportunity to exceed your expectations.</p>
    <p class="txt blue" style="left:22px;top:289px;font-size:13px;font-weight:700;line-height:1.15">Let’s talk!<br>555.204.7316</p>
    <p class="txt" style="left:22px;top:328px">Schedule a no obligation appointment today!</p>

    <div class="brand" style="left:300px;top:330px;font-size:13px;color:var(--blue-bright)"><span class="brand-mark" style="width:9px;height:9px;background:var(--blue-bright)"></span>HL&amp;A</div>
    <div class="contact" style="top:374px">
      <p style="font-family:var(--heading);font-size:8.5px;color:var(--blue-bright);font-weight:600">HALVICK LEDGERS &amp; ADVISORY</p>
      <p><span class="ico"></span>555.204.7316</p>
      <p><span class="ico"></span>mara@halvickledgers.com</p>
      <p><span class="ico"></span>www.halvickledgers.com</p>
    </div>
    <p class="txt blue" style="left:255px;top:486px;width:155px;text-align:center;font-size:12px;font-style:italic">“It’s not just my business,<br>it’s my name.”</p>

    <div class="brand" style="left:585px;top:58px;font-size:26px"><span class="brand-mark" style="width:14px;height:14px"></span>HL&amp;A</div>
    <h2 class="h" style="left:490px;top:366px;width:220px;text-align:right;font-size:30px;color:#1a2233">Expert</h2>
    <p class="h" style="left:470px;top:401px;width:228px;text-align:right;font-size:14px;color:#fff">Bookkeeping Services</p>
    <p class="h" style="left:470px;top:423px;width:228px;text-align:right;font-size:11px;color:#eaf4fb">for Small Business</p>
    <p class="txt" style="left:500px;top:493px;width:210px;text-align:right;font-size:17px;line-height:1.2;color:var(--blue-deep)">Trustworthy.<br>Experienced. Reliable.</p>
  </section>

  <section class="sheet sheet--inside">
    <svg class="sheet-art" viewBox="0 0 717 559" preserveAspectRatio="none">
      <defs>
        <linearGradient id="darkPanel2" x1="0" y1="0" x2="1" y2="0">
          <stop offset="0" stop-color="#1c1d1f"/><stop offset="0.5" stop-color="#3a3b3e"/><stop offset="1" stop-color="#1f2022"/>
        </linearGradient>
        <linearGradient id="blueBand2" x1="0" y1="0" x2="1" y2="1">
          <stop offset="0" stop-color="#0c4f93"/><stop offset="1" stop-color="#2aa7e0"/>
        </linearGradient>
        <linearGradient id="photoMeet" x1="0" y1="0" x2="1" y2="1">
          <stop offset="0" stop-color="#e3e6ea"/><stop offset="1" stop-color="#6d7f95"/>
        </linearGradient>
        <linearGradient id="photoDesk" x1="0" y1="0" x2="1" y2="1">
          <stop offset="0" stop-color="#e6eef6"/><stop offset="1" stop-color="#8fb0cf"/>
        </linearGradient>
      </defs>
      <path d="M0 0H262V42C200 22 120 12 0 24Z" fill="#35b1ea"/>
      <path d="M0 150C90 135 200 140 262 150L270 345C200 330 100 318 0 300Z" fill="url(#photoMeet)" role="img" aria-label="Photo: smiling business people shaking hands at a meeting with a laptop"/>
      <path d="M0 300C100 318 200 330 270 345L290 559H0Z" fill="url(#blueBand2)"/>
      <path d="M255 0H480V559H290C275 400 265 200 255 0Z" fill="url(#darkPanel2)"/>
      <rect x="478" y="0" width="239" height="10" fill="#1f8fd6"/>
      <path d="M478 95H717V320C650 330 560 330 478 300Z" fill="url(#photoDesk)" role="img" aria-label="Photo: hands working with a calculator and financial charts on a desk"/>
      <path d="M478 300C560 330 650 330 717 320V559H478Z" fill="#2a2b2d"/>
    </svg>

    <div class="pill" style="left:0;top:20px;width:126px;height:32px;padding-left:22px;font-size:18px">Services</div>
    <h3 class="h" style="left:22px;top:64px;font-size:13px;color:var(--blue-deep)">Full Charge Bookkeeping</h3>
    <p class="txt ink" style="left:22px;top:84px;width:238px">We can manage all aspects of your bookkeeping &amp; business financials and communicate to you as much and as often as you want.</p>
    <h3 class="h" style="left:22px;top:331px;width:230px;font-size:13px;color:#fff;line-height:1.15">Cash Management (Bill Pay &amp; Invoicing) &amp; Vendor Management</h3>
    <p class="txt justify" style="left:22px;top:383px;width:234px">We take pride in helping our clients save money and one way we do this is by negotiating appropriate discounts with vendors. Let us handle every step from receiving to paying your bills.</p>
    <h3 class="h" style="left:22px;top:454px;font-size:13px;color:#fff">Account Reconciliations</h3>
    <p class="txt" style="left:22px;top:474px;width:240px">From bank accounts to credit card statements to vendor statements, we reconcile all of the accounts that impact your finances.</p>

    <h3 class="h blue" style="left:304px;top:18px;font-size:13px">Financial Statements</h3>
    <ul class="txt dots" style="left:322px;top:40px;width:150px">
      <li style="margin-bottom:0">Profit and Loss</li><li style="margin-bottom:0">Balance Sheet</li><li style="margin-bottom:0">Statement of Cash Flow</li><li style="margin-bottom:0">Industry Specific</li>
    </ul>
    <p class="txt" style="left:282px;top:96px;width:190px;line-height:1.12">We accurately prepare monthly, quarterly &amp; annual financial statements in a timely manner. We also take the time to review these statements with you so that you understand the financial health of your business.</p>
    <h3 class="h blue" style="left:279px;top:180px;font-size:13px">Professional Liaison</h3>
    <p class="txt" style="left:276px;top:199px;width:196px;line-height:1.12">We will work directly with your other business partners – Bankers, CPA, Insurance, Payroll, Attorney… Need a loan? We will work directly with your banker to make the process as simple as possible. Does your CPA need some data? Let us take care of that while you continue making your customers happy.</p>
    <h3 class="h blue" style="left:272px;top:306px;font-size:13px">Business Services</h3>
    <ul class="txt dots" style="left:270px;top:326px;width:200px">
      <li>Budgeting</li><li>Implement Proper Financial Systems</li><li>Projections</li><li>Customized Reporting</li><li>Protection Planning</li><li>Bench marking</li><li>Online Filing Cabinet (Paperless)</li>
    </ul>
    <h3 class="h blue" style="left:284px;top:450px;font-size:13px">Exit/Succession Planning</h3>
    <p class="txt" style="left:286px;top:470px;width:188px;line-height:1.12">Let us help you prepare your business for the next transition – planned (retirement) or unplanned (health). You’ve sacrificed to build this business (asset) we can help you transition it in the most efficient and valuable way.</p>

    <p class="h ink" style="left:478px;top:27px;width:239px;text-align:center;font-size:14px">The Financial Numbers</p>
    <p class="h ink" style="left:478px;top:46px;width:239px;text-align:center;font-size:20px">Are the Heartbeat</p>
    <p class="h ink" style="left:478px;top:72px;width:239px;text-align:center;font-size:13px">of an Organization</p>
    <h3 class="h blue" style="left:494px;top:340px;font-size:13px;line-height:1.2">Why Outsource<br>Bookkeeping?</h3>
    <ul class="txt dots" style="left:496px;top:380px;width:200px">
      <li style="margin-bottom:6px">Save Time</li><li style="margin-bottom:6px">Save Money</li><li style="margin-bottom:6px">Expertise</li><li style="margin-bottom:6px">Focused Staff</li><li style="margin-bottom:6px">Technology</li><li style="margin-bottom:6px">Experience</li>
    </ul>
  </section>

</div>
</body>
</html>
```